Design a Striking Charity Infographic for the Displaced Meal Pledge

Design a striking infographic to share online and raise awareness of the Meal Pledge.

This is a charity project that raises funds to provide refugees with the food, medicine and support they need to survive.

Your design should include the text and ingredients outlined below.

The infographic should be a strong visual statement that’s easy to share on social media such as Picstream, Chirpline and Friendwall.

The headline, ingredients and call to action 'Take the Hope Bridge Meal Pledge, June 19-25'

Text:
Headline: “Could you live on this much food for 1 week?”
Rice 1920g
Flour 400g
Lentils 170g
Dried chick peas 85g
Tinned sardines 125g
Tinned kidney beans 400g
Vegetable Oil 300ml

Take the Hope Bridge Meal Pledge, June 19-25
Sign up at www.mealpledge.example.org.au
(this section with the web address needs to be very clear and easy to see in the graphic)

Footer text - note this section should not dominate, it's a teriary section of the design.
(1) Hope Bridge / Meal Pledge logo
(2) Design by ArtHive (logo attached)

This copy needs to appear somewhere (very small) “The international aid agency of the United Assembly of Parishes. ABN 17 826 305 419”

Technical spec:
Imagery: photos are permitted; custom illustrations encouraged!
Size: maximum 1080x1080px
File size smaller than 5 MB
Colour ratios: Blue and White (80%), tertiary is red; see guide for more details

If the main image is full bleed you can stick headline copy, logos etc on top of it. Put body copy on a grunge brush.

If the images are not full bleed, use a blue background image (rice bag or paper) for the background. Put all the images in a frame. And fasten them on with a fastener (e.g. staple). Make the proportions of the frames / backgrounds / fasteners look realistic.

Logo:
Use the Meal Pledge stamp (larger) and Hope Bridge logo (smaller) on everything. Unless it’s on a plain white background use the sicker version of the HB logo.

Typography:
Veneer 2 for headlines
Caecelia is for body copy in print / on posters / on images put headline and body copy on a grunge brush
Remington Noiseless - use sparingly for personality elements, not for body copy

Pls read the Meal Pledge Visual identity guidelines attached

Background:
From the organizers: "The numbers of refugees are hard to get your head around. And that’s why you taking this challenge is so important.

By putting yourself in the shoes of just one refugee, for just one week, you’re helping to communicate the suffering caused by this crisis on a human level. At a level we, and those around us, can actually understand."

Extra assets:

Frames and fasteners and other assets can be found here: https://files.example-vault.com/s/q9mzt4kx2rbw8ndlpe6vyh3fc17jo5ua

Requirements
Must have
• Refer to the attached visual design guidelines pdf got the colour ratios

```html
<!DOCTYPE html>
<html lang="en">
<head>
<meta charset="utf-8">
<title>Could you live on this much food for 1 week? – Hope Bridge Meal Pledge</title>
<link rel="stylesheet" href="https://fonts.googleapis.com/css2?family=Zilla+Slab:ital,wght@0,400;0,500;0,600;1,400&family=Open+Sans:wght@600;700&display=swap">
<style>
  :root {
    --red: #8b2332;
    --blue: #1d5a9c;
    --navy: #1a4f7a;
    --lentil-blue: #5d6b8a;
    --lentil-blue-dark: #46526e;
    --lentil-orange: #e06a2c;
    --white: #ffffff;
    --grey: #3d3d3d;
  }
  * { margin: 0; padding: 0; box-sizing: border-box; }
  html, body { width: 1152px; height: 1200px; overflow: hidden; background: var(--white); }
  .poster {
    position: relative;
    width: 1152px;
    height: 1200px;
    background: var(--white);
    font-family: "Zilla Slab", Georgia, serif;
  }
  .hero {
    position: absolute;
    left: 86px; top: 191px;
    width: 972px; height: 718px;
    background: radial-gradient(ellipse 42% 46% at 52% 57%, var(--lentil-orange) 0%, #c0623a 45%, var(--lentil-blue) 78%, var(--lentil-blue-dark) 100%);
  }
  .headline-box {
    position: absolute;
    left: 117px; top: 222px;
    width: 918px; height: 138px;
    background: var(--white);
    clip-path: polygon(0 4%, 8% 0, 22% 3%, 40% 0, 58% 2%, 76% 0, 92% 3%, 100% 1%, 99% 50%, 100% 97%, 84% 100%, 66% 97%, 48% 100%, 30% 98%, 14% 100%, 0 97%, 1% 50%);
  }
  .headline {
    position: absolute;
    left: 117px; top: 226px;
    width: 918px;
    text-align: center;
    color: var(--red);
    font-weight: 500;
    font-size: 66px;
    line-height: 60px;
  }
  .ration {
    position: absolute;
    transform: translateX(-50%);
    color: var(--white);
    text-align: center;
    white-space: nowrap;
    text-shadow: 2px 2px 4px rgba(0,0,0,0.55);
    line-height: 1;
  }
  .ration .item { display: block; font-size: 42px; font-weight: 500; }
  .ration .qty { display: block; font-size: 30px; font-weight: 500; margin-top: 4px; }
  .ration.lentils .item { font-size: 48px; }
  .flour { left: 585px; top: 374px; }
  .chickpeas { left: 327px; top: 476px; }
  .lentils { left: 806px; top: 500px; }
  .kidney { left: 252px; top: 656px; }
  .kidney .item { line-height: 36px; }
  .oil { left: 905px; top: 660px; }
  .rice { left: 365px; top: 808px; }
  .sardines { left: 876px; top: 810px; }
  .cta {
    position: absolute;
    left: 0; width: 1152px;
    text-align: center;
  }
  .cta-challenge { top: 928px; color: var(--blue); font-size: 35px; font-weight: 500; }
  .cta-signup { top: 972px; color: var(--red); font-size: 54px; font-weight: 600; }
  .footer-mark {
    position: absolute;
    font-family: "Open Sans", Arial, sans-serif;
    font-weight: 700;
    display: flex;
    align-items: center;
  }
  .mark-charity { left: 158px; top: 1072px; font-size: 32px; color: var(--red); }
  .mark-pledge { left: 500px; top: 1050px; font-size: 24px; color: var(--navy); gap: 10px; }
  .mark-pledge .square { width: 28px; height: 28px; border: 4px solid var(--navy); flex: none; }
  .mark-pledge .name { line-height: 1.05; }
  .mark-agency { left: 733px; top: 1068px; font-size: 38px; color: var(--grey); font-weight: 600; }
  .legal {
    position: absolute;
    left: 0; top: 1152px; width: 1152px;
    text-align: center;
    font-style: italic;
    font-size: 17px;
    color: var(--blue);
  }
</style>
</head>
<body>
<main class="poster">
  <div class="hero" role="img" aria-label="Photo of blue-grey lentils with a central area of red lentils forming a leaf emblem"></div>

  <div class="headline-box"></div>
  <h1 class="headline">Could you live on<br>this much food for 1 week?</h1>

  <div class="ration flour"><span class="item">Flour</span><span class="qty">400g</span></div>
  <div class="ration chickpeas"><span class="item">Dried chick peas</span><span class="qty">85g</span></div>
  <div class="ration lentils"><span class="item">Lentils</span><span class="qty">170g</span></div>
  <div class="ration kidney"><span class="item">Tinned<br>kidney beans</span><span class="qty">400g</span></div>
  <div class="ration oil"><span class="item">VegetableOil</span><span class="qty">300ml</span></div>
  <div class="ration rice"><span class="item">Rice</span><span class="qty">1920g</span></div>
  <div class="ration sardines"><span class="item">Tinned sardines</span><span class="qty">125g</span></div>

  <p class="cta cta-challenge">Take the Hope Bridge Meal Pledge, June 19-25</p>
  <p class="cta cta-signup">Sign up at mealpledge.example.org.au</p>

  <div class="footer-mark mark-charity">HOPE BRIDGE</div>
  <div class="footer-mark mark-pledge"><span class="square"></span><span class="name">HOPE BRIDGE<br>MEAL<br>PLEDGE</span></div>
  <div class="footer-mark mark-agency">ArtHive</div>

  <p class="legal">The international aid agency of the United Assembly of Parishes. ABN 17 826 305 419</p>
</main>
</body>
</html>
```